MODERN + COOL Business Card Needed!

SUMMARY
This is for a 40+ year old family business that is transitioning to the 2nd generation and is in real need of a more modern facelift. Ive attached a company logo (I made quickly as an idea with my limited PSD skills) to start off with that you are welcome to change and draw ideas from. Ive also attached some screen shots of cards I like to give you an idea of my preferences.

WHAT WE DO
The company name is Kin Dart HK Ltd. But I prefer to just call it Kin Dart or Kin Dart with Hong Kong as kind of a sub heading on the business card. We own a factory as well as help our customers find factories to make their product. Product I mean, toys 99.9% of the time. Simple old school toys like board games, puzzles, wooden toys, baby/infant toys.

You can say we are a "sourcing" or "trading" or "consulting" company with a factory to help you do it. But since we deal with toys, i like to keep it modern and cool and fun, not serious like managing hedge funds.

WHAT WE ARE LOOKING FOR
A cool, unique looking business card that stands out. In terms of design, something modern and professional. I like darker colored cards and I like colors such as blue/green/dark gray, but am open to other colored themes. I Like bright lime green with gray, always though thats a nice combo. I prefer cards that are all colored and not so much white showing (I think). Ive attached a few screenshots of cards so take a look to get a feel of what I like.

We do alot of wooden stacking games in variety of colors too like Pulto, Roni, Torvanets (google these to check them out). So designs that sort of resemble stacking or building would be cool but totally not necessary.

In terms of the physical aspects of the card, Im looking for a card a bit different than the standard rectangular shape. Double sided. Little things like having corner(s) be round or different angle instead of square edge I always thought was nice. Its got to be mostly a normal card size, no folding or smaller cards that fit weird in your wallet. No vertical designs. Am open to VERY different/creative shapes (as long as it still fits in a wallet good like a normal buisness card.

Hi everyone!

Just wanted to write a message to everyone to let them know all submissions are being reviewed or have been reviewed.  If I have not responded with feedback, rest assure your submission was definitely looked at in detail but I either have just been too busy to respond (alot of submissions!), or its on my to be considered list.

I respect and really enjoy receiving everyones creativity and work so I dont want it to go unrecognized - thus this message!  Feel free to submit more ideas if you like until this project ends.  Sometimes some designs just dont click but sometimes they can so you never know!

Thanks again for everyones participation and great work!

~Dov Ruel

Target Market(s)

The cards are mainly handed to toy company sourcers and buyers. People I talk to ... say Quelvin for example... might want to make their next edition of Farthundle game with a reputable factory at a good cost so they can sell it to stores at a profit.

So these are the types of people I often try to talk and introduce myself and my company to.

Industry/Entity Type

Building

Colors
acd036
0392cd
00a88e
474747
606060

Requirements
Must have
• Just double sided, not plain rectangle corners, and just cool to look at and catches your eye!

Oh and the obvious business card stuff like place for name, address, number, email, etc.
Nice to have
• Think more modern and fun, not serious and old fashion (thats what we used to be!). Can use the logo I attached and you can definitely alter and change the logo or make a whole new one!

Oh and can definitely use a creative slogan if you like to think of one based on what I described in what we do.
Should not have
• Dont use fonts or text placement that might make "Kin Dart" look like "Kind Art"... We arent selling news papers!!

Please nothing related to education since we have the word Dart in the title, thats not our business at all.

Logo and design should not be too heavy on things related to toys, as though thats what we primarily focus on now, what we do may change over time.

```html
<!DOCTYPE html>
<html lang="en">
<head>
<meta charset="utf-8">
<title>Kin Dart – Business Card</title>
<link rel="stylesheet" href="https://fonts.googleapis.com/css2?family=Comfortaa:wght@400;500&display=swap">
<style>
  :root {
    --stage: #ece8e3;
    --card-light: #f3f3f3;
    --card-dark: #3b3b3c;
    --brand-blue: #0aa8e6;
    --brand-green: #8dc63f;
    --text-light: #ffffff;
    --corner: 20px;
  }
  * { margin: 0; padding: 0; box-sizing: border-box; }
  html, body {
    width: 1200px;
    height: 723px;
    overflow: hidden;
    background: var(--stage);
    font-family: "Comfortaa", sans-serif;
  }
  .card {
    position: absolute;
    width: 451px;
    height: 260px;
    overflow: hidden;
    border-radius: var(--corner);
  }
  .card--front { left: 121px; top: 143px; background: var(--card-light); }
  .card--back  { left: 586px; top: 290px; background: var(--card-dark); }

  .pattern-field {
    position: absolute;
    left: 0;
    top: 0;
    height: 100%;
    background: linear-gradient(90deg, var(--brand-blue) 0%, var(--brand-green) 45%, var(--brand-blue) 80%, rgba(10,168,230,0) 100%);
  }
  .card--front .pattern-field { width: 184px; }
  .card--back .pattern-field { width: 182px; }

  .brand-mark {
    position: absolute;
    left: 282px;
    top: 72px;
    width: 58px;
    height: 58px;
    border-radius: 50%;
    background: var(--brand-green);
  }
  .brand-name {
    position: absolute;
    font-weight: 400;
    font-size: 42px;
    line-height: 1;
    letter-spacing: 1.5px;
    color: var(--brand-blue);
    white-space: nowrap;
  }
  .card--front .brand-name { left: 184px; right: 0; text-align: center; top: 159px; }
  .card--back .brand-name { right: 17px; top: 9px; }

  .contact {
    position: absolute;
    right: 18px;
    top: 58px;
    text-align: right;
    color: var(--text-light);
    font-size: 9.5px;
    line-height: 12px;
  }
  .contact__name, .contact__heading { font-size: 13px; line-height: 14px; }
  .contact__block--office { margin-top: 23px; }
  .contact__block--factory { margin-top: 12px; }
</style>
</head>
<body>
  <section class="card card--front" aria-label="Card front">
    <div class="pattern-field" role="img" aria-label="Blue and green halftone dot pattern fading from the left edge"></div>
    <div class="brand-mark"></div>
    <div class="brand-name">Kin Dart</div>
  </section>

  <section class="card card--back" aria-label="Card back">
    <div class="pattern-field" role="img" aria-label="Blue and green halftone dot pattern fading from the left edge"></div>
    <div class="brand-name">Kin Dart</div>
    <div class="contact">
      <div class="contact__block">
        <div class="contact__name">Dov Ruel</div>
        <div>Director/Founder</div>
        <div>DovRuel@kindarthk.com</div>
      </div>
      <div class="contact__block contact__block--office">
        <div class="contact__heading">Office</div>
        <div>18 Larkfield Row 12B</div>
        <div>Mid Level, Hong Kong</div>
        <div>Phone: (852)6230-4471</div>
      </div>
      <div class="contact__block contact__block--factory">
        <div class="contact__heading">Factory</div>
        <div>72 Heming Road,</div>
        <div>Linbao Ind. Zone</div>
        <div>Shanghai 201340, China</div>
        <div>Phone: (201) 5108 2264</div>
      </div>
    </div>
  </section>
</body>
</html>
```